Search Fund needs a PowerPoint template design

We need a eye-catching and compelling PowerPoint design for a new company based in Chicago called Tarn Ridge Partners. We are search fund with a primary mission to acquire a founder/family/entrepreneur owned businesses (This is similar to a Private Equity firm). Our goal is to offer investors a unique avenue to invest in an attractive business acquisition while providing business owners with an alternative path to exit. We would like the design to reflect crisp and professional nature that many financial firms present. The template should build on the design of the logo including expanding a logical color palette. The presentation will be used to describe facts regarding the firm, financial data and key messaging that we want our investors and potential partners to takeaway.

Target Market(s)

Financial Investors

Industry/Entity Type

Finance

Font styles to use
Serif
Sans Serif

Colors

Designer to choose colors to be used in the design.

Requirements
Must have
• Should include cover page and slide examples. Attractive data displays (graphs, charts, infographics etc.); Compelling cover; fly pages to put in between sections; table of contents page. Needs to have white space to add text.
Should not have
• Do not redesign the logo or change the logo colors. Additional colors should be added to the PowerPoint template

```html
<!DOCTYPE html>
<html lang="en">
<head>
<meta charset="utf-8">
<title>Tarn Ridge Partners – Presentation Template</title>
<link href="https://fonts.googleapis.com/css2?family=Open+Sans:ital,wght@0,400;0,600;0,700;0,800;1,800&display=swap" rel="stylesheet">
<style>
:root{
  --stage:#2e393e;
  --blue:#1c6cc0;
  --blue-dark:#0f4d96;
  --blue-mid:#2d8ad8;
  --blue-light:#45a8ea;
  --cyan:#6cc6f0;
  --ink:#222a30;
  --grey:#5b6168;
  --grey-light:#e9ecef;
  --white:#ffffff;
  --red:#d8322f;
  --green:#3aa53a;
}
*{box-sizing:border-box;margin:0;padding:0}
html,body{width:1200px;height:3249px;overflow:hidden}
body{background:var(--stage);font-family:"Open Sans",Arial,sans-serif;position:relative;color:var(--ink)}
.slide{position:absolute;width:552px;height:311px;overflow:hidden;background:var(--white)}
.abs{position:absolute}
.photo{position:absolute}
.title{position:absolute;left:0;right:0;text-align:center;font-weight:700;font-size:15px;color:var(--ink)}
.title .accent{color:var(--blue)}
.body{font-size:5.6px;line-height:1.45;color:var(--grey)}
.body b{color:var(--ink);font-weight:700;display:block;font-size:6px}
.brand-mark{position:absolute;right:14px;bottom:8px;font-size:7px;font-weight:700;color:var(--blue);letter-spacing:.3px}
.brand-mark.light{color:var(--white)}
.num-dot{position:absolute;width:16px;height:16px;border-radius:50%;background:var(--blue);color:#fff;font-size:8px;font-weight:700;display:flex;align-items:center;justify-content:center}
.agenda-line{position:absolute;height:1px;background:#c9d3dc}
.agenda-text{position:absolute;font-size:5.6px;color:var(--grey)}
.chevron{position:absolute;top:100px;height:78px;color:#fff}
.chevron .body{color:#fff}
.check{position:absolute;width:20px;height:20px;border-radius:50%;background:var(--blue);display:flex;align-items:center;justify-content:center}
.service-bar{position:absolute;height:24px;background:var(--blue);color:#fff;border-radius:3px;display:flex;align-items:center;padding:0 8px}
.service-bar .body{color:#fff;font-size:5px}
.price-card{position:absolute;top:75px;width:98px;height:170px;background:#fff;border-radius:4px;box-shadow:0 3px 8px rgba(0,0,0,.22);overflow:hidden}
.price-card .plan{font-size:5.5px;font-weight:700;text-align:center;margin-top:8px}
.price-card .price{font-size:15px;font-weight:700;text-align:center;color:var(--ink)}
.price-card .price small{font-size:6px;font-weight:400}
.price-card .row{font-size:5px;color:var(--grey);text-align:center;border-top:1px solid #eee;padding:3px 0}
.price-card .foot{position:absolute;bottom:0;left:0;right:0;height:10px;background:var(--blue-mid)}
table.data{position:absolute;border-collapse:collapse;font-size:5.5px;color:var(--grey)}
table.data th{color:#fff;font-weight:600;padding:3px 4px;font-size:5px}
table.data td{padding:5px 4px;text-align:center;border-bottom:1px solid #dde2e6}
table.data td.label{text-align:left;background:#f0f2f4;color:var(--ink)}
.cmp-col{position:absolute;top:112px;width:44px;height:140px;border-radius:4px;background:#fff;box-shadow:0 2px 6px rgba(0,0,0,.2)}
.cmp-head{position:absolute;top:100px;width:44px;height:14px;border-radius:3px;color:#fff;font-size:5px;font-weight:700;display:flex;align-items:center;justify-content:center}
.cmp-label{position:absolute;left:22px;width:100px;height:12px;background:#e4e7ea;font-size:5px;color:var(--ink);display:flex;align-items:center;padding-left:5px}
.mark{position:absolute;font-size:10px;font-weight:800;width:44px;text-align:center}
.mark.no{color:var(--red)} .mark.yes{color:var(--green)}
.donut-label{position:absolute;top:130px;width:76px;text-align:center;color:#fff}
.donut-label .body{color:#e6f1fb}
.donut-label b{color:#fff}
.contact{position:absolute;font-size:6.5px;color:#fff;display:flex;align-items:center;gap:4px}
.contact i{display:inline-block;width:9px;height:9px;border-radius:50%;background:#fff}
</style>
</head>
<body>

<!-- Row 1 -->
<section class="slide cover" style="left:22px;top:26px">
  <div class="photo" role="img" aria-label="Upward view of glass skyscrapers against a pale sky" style="inset:0;background:radial-gradient(ellipse at 50% 45%,#f4f7fa 0%,#c8d2dc 35%,#6c7886 75%,#3d4753 100%)"></div>
  <div class="abs" style="left:0;right:0;top:140px;text-align:center;font-size:20px;font-weight:800;color:var(--blue);letter-spacing:.5px">Tarn Ridge Partners</div>
</section>

<section class="slide" style="left:626px;top:26px">
  <div class="photo" role="img" aria-label="Dim desk scene with a hand on a laptop and a wristwatch" style="inset:0;background:linear-gradient(120deg,#4a5058 0%,#7c848e 45%,#3a3f46 100%)"></div>
  <div class="abs" style="left:130px;top:98px;width:292px;height:86px;background:rgba(255,255,255,.72);display:flex;align-items:center;justify-content:center;font-size:29px;font-weight:600;color:#4d545b">Section Break</div>
</section>

<!-- Row 2 -->
<section class="slide" style="left:22px;top:347px">
  <div class="photo" role="img" aria-label="Tall glass tower seen from below in blue tones" style="inset:0;background:linear-gradient(180deg,#2f6fc4 0%,#4b8fda 40%,#8fb9e6 100%)"></div>
  <div class="abs" style="left:0;right:0;top:60px;text-align:center;font-size:34px;font-weight:800;font-style:italic;color:#fff;letter-spacing:.5px">SECTION BREAK</div>
</section>

<section class="slide" style="left:626px;top:347px">
  <div class="photo" role="img" aria-label="Office towers reaching into a cloudy sky" style="inset:0 260px 0 0;clip-path:polygon(0 0,100% 0,85% 50%,100% 100%,0 100%);background:linear-gradient(160deg,#c9d6e2 0%,#5d6c7c 55%,#2c3540 100%)"></div>
  <div class="abs" style="left:330px;top:18px;font-size:17px;font-weight:700;color:var(--blue)">Agenda</div>
  <div class="num-dot" style="left:292px;top:58px">1</div><div class="agenda-line" style="left:312px;top:66px;width:200px"></div><div class="agenda-text" style="left:318px;top:60px">Firm overview and mission</div>
  <div class="num-dot" style="left:304px;top:90px">2</div><div class="agenda-line" style="left:324px;top:98px;width:188px"></div><div class="agenda-text" style="left:330px;top:92px">Investment thesis</div>
  <div class="num-dot" style="left:314px;top:122px">3</div><div class="agenda-line" style="left:334px;top:130px;width:178px"></div><div class="agenda-text" style="left:340px;top:124px">Target profile</div>
  <div class="num-dot" style="left:314px;top:154px">4</div><div class="agenda-line" style="left:334px;top:162px;width:178px"></div><div class="agenda-text" style="left:340px;top:156px">Search process</div>
  <div class="num-dot" style="left:304px;top:186px">5</div><div class="agenda-line" style="left:324px;top:194px;width:188px"></div><div class="agenda-text" style="left:330px;top:188px">Financial outlook</div>
  <div class="num-dot" style="left:292px;top:218px">6</div><div class="agenda-line" style="left:312px;top:226px;width:200px"></div><div class="agenda-text" style="left:318px;top:220px">Next steps</div>
  <div class="brand-mark">TARN RIDGE</div>
</section>

<!-- Row 3 -->
<section class="slide" style="left:22px;top:668px">
  <div class="abs" style="left:0;top:0;width:18px;height:311px;background:var(--blue)"></div>
  <div class="abs" style="left:4px;top:230px;transform:rotate(-90deg);transform-origin:left top;font-size:6px;color:#fff;font-weight:700;white-space:nowrap">Your Text Here</div>
  <div class="abs body" style="left:26px;top:40px;width:120px"><b style="font-size:8px">Lorem ipsum dolor sit amet.</b><br>Our search fund partners with owners who want a thoughtful exit. We study each business closely, respect its history and plan for steady growth. Investors gain direct access to a single well run company with clear reporting and shared goals over the long term.</div>
  <div class="photo" role="img" aria-label="Close view of a tablet showing financial figures" style="left:170px;top:0;width:210px;height:311px;background:linear-gradient(135deg,#1d2a3a 0%,#2c5d86 50%,#52b2d8 100%)"></div>
  <div class="abs body" style="left:395px;top:48px;width:140px">
    <div style="margin-bottom:18px">Deep sector research guides every review we run.</div>
    <div style="margin-bottom:18px">Patient capital supports the owner transition.</div>
    <div style="margin-bottom:18px">Clear terms keep each party well informed.</div>
    <div>Active governance drives lasting value.</div>
  </div>
  <svg class="abs" style="left:420px;top:36px" width="12" height="220" viewBox="0 0 12 220" fill="none" stroke="#1c6cc0" stroke-width="1.2"><rect x="2" y="2" width="8" height="8"/><path d="M1 56h3l2 6h5l1-4H5"/><circle cx="6" cy="108" r="4"/><circle cx="5" cy="158" r="3.5"/><path d="M8 161l3 3"/></svg>
  <div class="brand-mark" style="font-size:6px">TARN RIDGE</div>
</section>

<section class="slide" style="left:626px;top:668px">
  <div class="abs" style="left:0;top:0;width:552px;height:150px;background:linear-gradient(90deg,#1c6cc0,#45a8ea)"></div>
  <div class="abs" style="left:20px;top:52px;width:200px;height:26px;background:#fff;transform:rotate(-6deg);display:flex;align-items:center;padding-left:10px;font-size:14px;font-weight:700;color:var(--ink)">Lorem ipsum&nbsp;<span style="color:var(--blue);font-weight:600;font-size:11px">dolor</span></div>
  <div class="abs body" style="left:240px;top:34px;width:280px;color:#eaf4fc">We acquire established, founder owned companies and hold them for the long run. Our team brings operating skill, patient capital and a clear plan to every deal. We aim for steady growth, fair terms for sellers and open reporting to every partner who joins our fund from the start.</div>
  <div class="check" style="left:32px;top:178px"><svg width="10" height="8"><path d="M1 4l3 3 5-6" stroke="#fff" stroke-width="1.6" fill="none"/></svg></div>
  <div class="abs body" style="left:60px;top:177px;width:140px"><b>Lorem ipsum dolor</b>Strong cash flow and loyal customers.</div>
  <div class="check" style="left:32px;top:222px;background:var(--blue-dark)"><svg width="10" height="8"><path d="M1 4l3 3 5-6" stroke="#fff" stroke-width="1.6" fill="none"/></svg></div>
  <div class="abs body" style="left:60px;top:221px;width:140px"><b>Lorem ipsum dolor</b>Experienced teams ready to grow.</div>
  <div class="check" style="left:300px;top:178px;background:var(--blue-light)"><svg width="10" height="8"><path d="M1 4l3 3 5-6" stroke="#fff" stroke-width="1.6" fill="none"/></svg></div>
  <div class="abs body" style="left:328px;top:177px;width:140px"><b>Lorem ipsum dolor</b>Sound margins in stable markets.</div>
  <div class="check" style="left:300px;top:222px;background:var(--cyan)"><svg width="10" height="8"><path d="M1 4l3 3 5-6" stroke="#fff" stroke-width="1.6" fill="none"/></svg></div>
  <div class="abs body" style="left:328px;top:221px;width:140px"><b>Lorem ipsum dolor</b>Clear path to a smooth handover.</div>
  <div class="brand-mark" style="font-size:6px">TARN RIDGE</div>
</section>

<!-- Row 4 -->
<section class="slide" style="left:22px;top:989px">
  <div class="title" style="top:36px">Lorem ipsum <span class="accent">dolor</span></div>
  <svg class="abs" style="left:18px;top:96px" width="516" height="90" viewBox="0 0 516 90">
    <polygon points="0,0 118,0 138,45 118,90 0,90 18,45" fill="#0f4d96"/>
    <polygon points="126,0 244,0 264,45 244,90 126,90 146,45" fill="#1c6cc0"/>
    <polygon points="252,0 370,0 390,45 370,90 252,90 272,45" fill="#2d8ad8"/>
    <polygon points="378,0 496,0 516,45 496,90 378,90 398,45" fill="#6cc6f0"/>
    <g fill="#fff"><rect x="55" y="18" width="4" height="12"/><rect x="61" y="13" width="4" height="17"/><rect x="67" y="8" width="4" height="22"/>
    <rect x="182" y="8" width="16" height="22" rx="2" fill="none" stroke="#fff" stroke-width="1.5"/>
    <circle cx="320" cy="19" r="11"/><path d="M440 30c0-7 4-10 9-10s9 3 9 10z"/><circle cx="449" cy="14" r="5"/></g>
    <path d="M320 19V8a11 11 0 0 1 11 11z" fill="#2d8ad8"/>
  </svg>
  <div class="abs body" style="left:58px;top:134px;width:80px;color:#fff"><b style="color:#fff">Lorem ipsum dolor</b>Focused search in sectors we know well.</div>
  <div class="abs body" style="left:184px;top:134px;width:80px;color:#fff"><b style="color:#fff">Lorem ipsum dolor</b>Careful review of each target firm.</div>
  <div class="abs body" style="left:310px;top:134px;width:80px;color:#fff"><b style="color:#fff">Lorem ipsum dolor</b>Fair offers built on shared value.</div>
  <div class="abs body" style="left:436px;top:134px;width:80px;color:#fff"><b style="color:#fff">Lorem ipsum dolor</b>Hands on growth after closing.</div>
  <div class="brand-mark" style="font-size:6px">TARN RIDGE</div>
</section>

<section class="slide" style="left:626px;top:989px">
  <div class="photo" role="img" aria-label="Hands typing on a laptop showing a data dashboard" style="left:0;top:0;width:245px;height:311px;background:linear-gradient(135deg,#6b4a34 0%,#3b3632 45%,#1c2430 100%)"></div>
  <div class="abs" style="left:245px;top:0;width:34px;height:311px;background:var(--blue)"></div>
  <div class="abs" style="left:296px;top:44px;font-size:14px;font-weight:700">Lorem ipsum <span style="color:var(--blue)">dolor</span></div>
  <div class="abs body" style="left:296px;top:68px;width:236px">We look for companies with a proven model, loyal clients and a team that wants to keep building. Our partners bring patient capital and years of hands on skill.<br><br>Every deal is guided by careful research, honest terms and a clear plan for the first hundred days after closing.<br><br>Investors receive steady updates, full access to results and a direct voice in key choices.<br><br>Sellers gain a trusted buyer who will respect the legacy they worked hard to build.</div>
  <div class="brand-mark" style="font-size:6px">TARN RIDGE</div>
</section>

<!-- Row 5 -->
<section class="slide" style="left:22px;top:1310px">
  <div class="title" style="top:44px">Lorem ipsum <span class="accent">dolor</span></div>
  <div class="abs" style="left:0;top:84px;width:552px;height:200px;background:#eceef0"></div>
  <svg class="abs" style="left:246px;top:160px" width="60" height="84" viewBox="0 0 60 84" fill="none" stroke="#1c6cc0" stroke-width="2.5">
    <path d="M30 14a18 18 0 0 0-10 33v10h20V47a18 18 0 0 0-10-33z" fill="#2d8ad8" stroke="none"/>
    <path d="M20 62h20M22 68h16M25 74h10" /><path d="M30 2v6M8 12l5 4M52 12l-5 4M2 34h6M52 34h6"/>
  </svg>
  <div class="abs body" style="left:236px;top:100px;width:80px;text-align:center"><b>Lorem ipsum dolor</b>Clear value plan.</div>
  <div class="abs body" style="left:96px;top:130px;width:120px;text-align:right"><b>Lorem ipsum dolor</b>Sound research on each target sector.</div>
  <div class="abs body" style="left:66px;top:178px;width:130px;text-align:right"><b>Lorem ipsum dolor</b>Trusted ties with local owners.</div>
  <div class="abs body" style="left:336px;top:130px;width:120px"><b>Lorem ipsum dolor</b>Strong network of skilled advisers.</div>
  <div class="abs body" style="left:356px;top:178px;width:130px"><b>Lorem ipsum dolor</b>Aligned goals for all partners.</div>
  <div class="brand-mark" style="font-size:6px">TARN RIDGE</div>
</section>

<section class="slide" style="left:626px;top:1310px">
  <div class="title" style="top:36px">Lorem ipsum <span class="accent">dolor</span></div>
  <svg class="abs" style="left:176px;top:72px" width="200" height="200" viewBox="0 0 200 200">
    <g fill="#2d8ad8"><polygon points="100,0 130,28 115,28 115,80 85,80 85,28 70,28"/><polygon points="200,100 172,130 172,115 120,115 120,85 172,85 172,70" fill="#6cc6f0"/><polygon points="100,200 70,172 85,172 85,120 115,120 115,172 130,172" fill="#1c6cc0"/><polygon points="0,100 28,70 28,85 80,85 80,115 28,115 28,130" fill="#0f4d96"/></g>
    <g fill="#fff" font-size="7" font-family="Open Sans, sans-serif" text-anchor="middle"><text x="100" y="44">This is</text><text x="100" y="52">a sample</text><text x="100" y="60">text</text><text x="100" y="150">This is</text><text x="100" y="158">a sample</text><text x="100" y="166">text</text><text x="150" y="98">This is</text><text x="150" y="106">sample</text><text x="52" y="98">This is a</text><text x="52" y="106">sample text</text></g>
    <g fill="#fff" font-size="12" font-weight="700" font-family="Open Sans, sans-serif"><text x="104" y="24">1</text><text x="180" y="124">2</text><text x="96" y="188">4</text><text x="14" y="124">3</text></g>
  </svg>
  <div class="abs body" style="left:30px;top:80px;width:140px">We screen hundreds of firms each year and pick only those that match our clear set of goals.</div>
  <div class="abs body" style="left:30px;top:200px;width:140px">Each target gets a full review of cash flow, customers, staff and growth room.</div>
  <div class="abs body" style="left:384px;top:80px;width:140px">Owners stay involved as long as they wish and help guide a smooth transfer of duties.</div>
  <div class="abs body" style="left:384px;top:200px;width:140px">Investors share in the upside with simple terms and steady reports on results.</div>
  <div class="brand-mark" style="font-size:6px">TARN RIDGE</div>
</section>

<!-- Row 6 -->
<section class="slide" style="left:22px;top:1631px">
  <div class="title" style="top:34px;font-size:14px">Sed ut perspiciatis unde</div>
  <svg class="abs" style="left:176px;top:96px" width="200" height="50" viewBox="0 0 200 50">
    <circle cx="25" cy="25" r="24" fill="#1c6cc0"/><circle cx="175" cy="25" r="24" fill="#2d8ad8"/>
    <circle cx="25" cy="25" r="7" fill="none" stroke="#fff" stroke-width="2"/>
    <path d="M165 17h3l3 11h10l2-7h-13" fill="none" stroke="#fff" stroke-width="2"/><circle cx="172" cy="32" r="1.5" fill="#fff"/><circle cx="180" cy="32" r="1.5" fill="#fff"/>
    <path d="M80 20h40l-6-6M120 30H80l6 6" fill="none" stroke="#aab4bd" stroke-width="2.5"/>
  </svg>
  <div class="abs" style="left:110px;top:112px;font-size:6px;font-weight:700;color:var(--blue);text-align:center;width:60px">Your Business<br>Here</div>
  <div class="abs" style="left:382px;top:112px;font-size:6px;font-weight:700;color:var(--blue);text-align:center;width:60px">Your Business<br>Here</div>
  <div class="abs" style="left:0;right:0;top:168px;text-align:center;font-size:18px;font-weight:700;color:var(--blue)">65,190.00</div>
  <div class="brand-mark" style="font-size:6px">TARN RIDGE</div>
</section>

<section class="slide" style="left:626px;top:1631px">
  <div class="service-bar" style="left:28px;top:48px;width:150px"><span class="body">Capital sourced from trusted partners</span></div>
  <div class="service-bar" style="left:28px;top:80px;width:150px;background:var(--blue-dark)"><span class="body">Owner transition and succession plans</span></div>
  <div class="service-bar" style="left:28px;top:112px;width:150px;background:var(--blue-mid)"><span class="body">Growth strategy for each portfolio firm</span></div>
  <div class="service-bar" style="left:28px;top:144px;width:150px;background:var(--blue-light)"><span class="body">Clear reporting to every investor</span></div>
  <div class="service-bar" style="left:28px;top:176px;width:150px;background:var(--cyan)"><span class="body">Ongoing support after closing</span></div>
  <div class="service-bar" style="left:374px;top:48px;width:150px"><span class="body">Market research and deal sourcing</span></div>
  <div class="service-bar" style="left:374px;top:80px;width:150px;background:var(--blue-dark)"><span class="body">Careful due diligence on each target</span></div>
  <div class="service-bar" style="left:374px;top:112px;width:150px;background:var(--blue-mid)"><span class="body">Fair deal terms built with sellers</span></div>
  <div class="service-bar" style="left:374px;top:144px;width:150px;background:var(--blue-light)"><span class="body">Operating help from seasoned leaders</span></div>
  <div class="service-bar" style="left:374px;top:176px;width:150px;background:var(--cyan)"><span class="body">Long term value for all partners</span></div>
  <div class="abs" style="left:172px;top:34px;width:208px;height:190px;background:#fff;box-shadow:0 3px 12px rgba(0,0,0,.3);padding:36px 20px 0">
    <div style="font-size:9px;font-weight:700;text-align:center;margin-bottom:6px">Our Services</div>
    <div class="body" style="text-align:center">We guide each deal from first call to final close and stay on as active owners. Our team offers capital, skill and a steady hand so every firm can keep growing.</div>
  </div>
  <div class="brand-mark" style="font-size:6px">TARN RIDGE</div>
</section>

<!-- Row 7 -->
<section class="slide" style="left:22px;top:1952px">
  <div class="title" style="top:32px">Lorem ipsum <span class="accent">dolor</span></div>
  <div class="price-card" style="left:46px"><div class="plan">Lorem ipsum</div><div class="price">$10<small>.00</small></div><div class="row">Item one</div><div class="row">Item two</div><div class="row">Item three</div><div class="row">Item four</div><div class="row">Item five</div><div class="foot"></div></div>
  <div class="price-card" style="left:166px"><div class="plan">Lorem ipsum</div><div class="price">$99<small>.00</small></div><div class="row">Item one</div><div class="row">Item two</div><div class="row">Item three</div><div class="row">Item four</div><div class="row">Item five</div><div class="foot"></div></div>
  <div class="price-card" style="left:286px"><div class="plan">Lorem ipsum</div><div class="price">$100<small>.00</small></div><div class="row">Item one</div><div class="row">Item two</div><div class="row">Item three</div><div class="row">Item four</div><div class="row">Item five</div><div class="foot"></div></div>
  <div class="price-card" style="left:406px"><div class="plan">Lorem ipsum</div><div class="price">$199<small>.00</small></div><div class="row">Item one</div><div class="row">Item two</div><div class="row">Item three</div><div class="row">Item four</div><div class="row">Item five</div><div class="foot"></div></div>
  <div class="brand-mark" style="font-size:6px">TARN RIDGE</div>
</section>

<section class="slide" style="left:626px;top:1952px">
  <div class="title" style="top:28px">Lorem ipsum <span class="accent" style="color:#c0392b">dolor</span></div>
  <table class="data" style="left:30px;top:60px;width:494px">
    <tr><th style="background:none"></th><th style="background:var(--blue-dark)">Lorem ipsum</th><th style="background:var(--blue)">Lorem ipsum</th><th style="background:var(--blue-mid)">Lorem ipsum</th><th style="background:var(--blue-light)">Lorem ipsum</th><th style="background:var(--cyan)">Lorem ipsum</th></tr>
    <tr><td class="label">Lorem ipsum dolor sit amet</td><td>23</td><td>45</td><td>4</td><td>4</td><td>34</td></tr>
    <tr><td class="label">Lorem ipsum dolor sit amet</td><td>234</td><td>75</td><td>4</td><td>4</td><td>86</td></tr>
    <tr><td class="label">Lorem ipsum dolor sit amet</td><td>55</td><td>75</td><td>64</td><td>8</td><td>44</td></tr>
    <tr><td class="label">Lorem ipsum dolor sit amet</td><td>66</td><td>45</td><td>4</td><td>4</td><td>44</td></tr>
    <tr><td class="label">Lorem ipsum dolor sit amet</td><td>78</td><td>64</td><td>46</td><td>6</td><td>24</td></tr>
    <tr><td class="label">Lorem ipsum dolor sit amet</td><td>56</td><td>46</td><td>44</td><td>3</td><td>55</td></tr>
  </table>
  <div class="brand-mark" style="font-size:6px">TARN RIDGE</div>
</section>

<!-- Row 8 -->
<section class="slide" style="left:22px;top:2273px">
  <div class="title" style="top:32px">Lorem ipsum <span class="accent">dolor</span></div>
  <div class="cmp-head" style="left:160px;background:var(--blue-dark)">Lorem ipsum</div>
  <div class="cmp-head" style="left:232px;background:var(--blue)">Lorem ipsum</div>
  <div class="cmp-head" style="left:304px;background:var(--blue-mid)">Lorem ipsum</div>
  <div class="cmp-head" style="left:376px;background:var(--blue-light)">Lorem ipsum</div>
  <div class="cmp-head" style="left:448px;background:var(--cyan)">Lorem ipsum</div>
  <div class="cmp-col" style="left:160px"></div><div class="cmp-col" style="left:232px"></div><div class="cmp-col" style="left:304px"></div><div class="cmp-col" style="left:376px"></div><div class="cmp-col" style="left:448px"></div>
  <div class="cmp-label" style="top:124px">Lorem ipsum dolor sit amet</div>
  <div class="cmp-label" style="top:146px">Lorem ipsum dolor sit amet</div>
  <div class="cmp-label" style="top:168px">Lorem ipsum dolor sit amet</div>
  <div class="cmp-label" style="top:190px">Lorem ipsum dolor sit amet</div>
  <div class="cmp-label" style="top:212px">Lorem ipsum dolor sit amet</div>
  <div class="mark yes" style="left:160px;top:120px">+</div><div class="mark no" style="left:232px;top:120px">×</div><div class="mark no" style="left:304px;top:120px">×</div><div class="mark yes" style="left:376px;top:120px">+</div><div class="mark yes" style="left:448px;top:120px">+</div>
  <div class="mark no" style="left:160px;top:142px">×</div><div class="mark no" style="left:232px;top:142px">×</div><div class="mark yes" style="left:304px;top:142px">+</div><div class="mark no" style="left:376px;top:142px">×</div><div class="mark yes" style="left:448px;top:142px">+</div>
  <div class="mark no" style="left:160px;top:164px">×</div><div class="mark yes" style="left:232px;top:164px">+</div><div class="mark no" style="left:304px;top:164px">×</div><div class="mark no" style="left:376px;top:164px">×</div><div class="mark no" style="left:448px;top:164px">×</div>
  <div class="mark yes" style="left:160px;top:186px">+</div><div class="mark no" style="left:232px;top:186px">×</div><div class="mark yes" style="left:304px;top:186px">+</div><div class="mark yes" style="left:376px;top:186px">+</div><div class="mark no" style="left:448px;top:186px">×</div>
  <div class="mark no" style="left:160px;top:208px">×</div><div class="mark yes" style="left:232px;top:208px">+</div><div class="mark no" style="left:304px;top:208px">×</div><div class="mark no" style="left:376px;top:208px">×</div><div class="mark no" style="left:448px;top:208px">×</div>
  <div class="brand-mark" style="font-size:6px">TARN RIDGE</div>
</section>

<section class="slide" style="left:626px;top:2273px">
  <div class="title" style="top:26px;font-size:14px;line-height:1.2">Sed ut perspiciatis, unde<br><span class="accent">omnis iste natus</span></div>
  <div class="abs" style="left:44px;top:94px;font-size:32px;font-weight:600;color:#8d949a">250K</div>
  <div class="abs body" style="left:134px;top:98px;width:210px"><b>Sed ut perspiciatis</b>Total capital raised across our first search round.</div>
  <svg class="abs" style="left:50px;top:150px" width="310" height="80" viewBox="0 0 310 80">
    <rect x="0" y="4" width="200" height="6" fill="#0f4d96"/><rect x="0" y="14" width="250" height="6" fill="#45a8ea"/><rect x="0" y="24" width="150" height="6" fill="#1c6cc0"/><rect x="0" y="34" width="120" height="6" fill="#6cc6f0"/><rect x="0" y="44" width="180" height="6" fill="#2d8ad8"/>
    <line x1="0" y1="58" x2="300" y2="58" stroke="#aab4bd"/>
    <g font-size="5" fill="#5b6168" font-family="Open Sans, sans-serif"><text x="0" y="66">1</text><text x="37" y="66">2</text><text x="75" y="66">3</text><text x="112" y="66">4</text><text x="150" y="66">5</text><text x="187" y="66">6</text><text x="225" y="66">7</text><text x="262" y="66">8</text></g>
  </svg>
  <div class="abs" style="left:366px;top:144px;width:160px;height:80px;background:var(--blue);clip-path:polygon(12% 0,100% 0,100% 100%,12% 100%,0 50%);padding:10px 10px 0 30px">
    <div class="body" style="color:#fff">Our fund targets firms with strong cash flow and room to grow. Each deal is sized for steady returns and low debt risk.</div>
  </div>
  <div class="brand-mark" style="font-size:6px">TARN RIDGE</div>
</section>

<!-- Row 9 -->
<section class="slide" style="left:22px;top:2594px;background:linear-gradient(180deg,#2a78cc,#45a8ea)">
  <div class="title" style="top:44px;color:#fff;font-size:14px">Sed ut perspiciatis, unde omnis iste natus</div>
  <svg class="abs" style="left:0;top:92px" width="552" height="50" viewBox="0 0 552 50">
    <g fill="#fff"><circle cx="70" cy="24" r="20"/><circle cx="170" cy="24" r="20"/><circle cx="276" cy="24" r="20"/><circle cx="382" cy="24" r="20"/><circle cx="482" cy="24" r="20"/></g>
    <g fill="none" stroke-width="6">
      <circle cx="70" cy="24" r="20" stroke="#f5c518" stroke-dasharray="69 126" transform="rotate(-90 70 24)"/>
      <circle cx="170" cy="24" r="20" stroke="#3aa53a" stroke-dasharray="25 126" transform="rotate(-90 170 24)"/>
      <circle cx="276" cy="24" r="20" stroke="#9b2fc9" stroke-dasharray="69 126" transform="rotate(-90 276 24)"/>
      <circle cx="382" cy="24" r="20" stroke="#e0245e" stroke-dasharray="82 126" transform="rotate(-90 382 24)"/>
      <circle cx="482" cy="24" r="20" stroke="#1c6cc0" stroke-dasharray="6 126" transform="rotate(-90 482 24)"/>
    </g>
    <g font-size="6" fill="#5b6168" text-anchor="middle" font-family="Open Sans, sans-serif"><text x="70" y="26">55%</text><text x="170" y="26">20%</text><text x="276" y="26">55%</text><text x="382" y="26">65%</text><text x="482" y="26">5%</text></g>
  </svg>
  <div class="donut-label" style="left:32px"><div class="body"><b>Lorem ipsum dolor</b>Share of revenue from repeat clients.</div></div>
  <div class="donut-label" style="left:132px"><div class="body"><b>Lorem ipsum dolor</b>Annual growth in core service lines.</div></div>
  <div class="donut-label" style="left:238px"><div class="body"><b>Lorem ipsum dolor</b>Gross margin across target sectors.</div></div>
  <div class="donut-label" style="left:344px"><div class="body"><b>Lorem ipsum dolor</b>Owners open to a planned exit.</div></div>
  <div class="donut-label" style="left:444px"><div class="body"><b>Lorem ipsum dolor</b>Average annual staff turnover.</div></div>
  <div class="brand-mark light" style="font-size:6px">TARN RIDGE</div>
</section>

<section class="slide" style="left:626px;top:2594px;background:linear-gradient(180deg,#1c6cc0,#45a8ea)">
  <div class="title" style="top:26px;color:#fff;font-size:14px;line-height:1.2">Sed ut perspiciatis, unde omnis<br>iste natus</div>
  <svg class="abs" style="left:30px;top:74px" width="500" height="140" viewBox="0 0 500 140">
    <g stroke="rgba(255,255,255,.35)" stroke-width=".7"><line x1="20" y1="5" x2="490" y2="5"/><line x1="20" y1="25" x2="490" y2="25"/><line x1="20" y1="45" x2="490" y2="45"/><line x1="20" y1="65" x2="490" y2="65"/><line x1="20" y1="85" x2="490" y2="85"/><line x1="20" y1="105" x2="490" y2="105"/></g>
    <line x1="20" y1="120" x2="490" y2="120" stroke="#fff" stroke-width=".8"/>
    <polyline points="30,80 100,60 170,70 240,45 310,62 380,40 450,48 480,30" fill="none" stroke="#d8322f" stroke-width="1.6"/>
    <polyline points="30,100 100,85 170,95 240,78 310,90 380,72 450,82 480,70" fill="none" stroke="#fff" stroke-width="1.4"/>
    <g font-size="5" fill="#fff" font-family="Open Sans, sans-serif"><text x="0" y="8">8000</text><text x="0" y="48">6000</text><text x="0" y="88">4000</text><text x="0" y="122">0</text>
    <text x="30" y="130">Item 1</text><text x="100" y="130">Item 2</text><text x="170" y="130">Item 3</text><text x="240" y="130">Item 4</text><text x="310" y="130">Item 5</text><text x="380" y="130">Item 6</text><text x="450" y="130">Item 7</text></g>
  </svg>
  <div class="abs" style="left:34px;top:230px;font-size:16px;font-weight:700;color:#fff">57%</div>
  <div class="abs body" style="left:80px;top:230px;width:150px;color:#e6f1fb"><b style="color:#fff">Contents Title</b>Share of targets that pass our first stage review.</div>
  <div class="abs" style="left:290px;top:230px;font-size:16px;font-weight:700;color:#fff">79%</div>
  <div class="abs body" style="left:336px;top:230px;width:170px;color:#e6f1fb"><b style="color:#fff">Contents Title</b>Share of owners who stay on through the handover.</div>
  <div class="brand-mark light" style="font-size:6px">TARN RIDGE</div>
</section>

<!-- Row 10 -->
<section class="slide" style="left:22px;top:2915px">
  <div class="title" style="top:28px;font-size:14px;line-height:1.2">Sed ut perspiciatis, unde<br><span class="accent">omnis iste natus</span></div>
  <div class="abs" style="left:24px;top:86px;width:170px;height:172px;background:var(--blue);padding:12px">
    <div class="body" style="color:#fff">Our search fund studies each market before we make an offer. We weigh risk, cash flow and growth room.<br><br>Investors get a clear view of every deal, with simple terms and honest updates on how the business is doing over time.</div>
  </div>
  <svg class="abs" style="left:240px;top:70px" width="280" height="130" viewBox="0 0 280 130">
    <line x1="10" y1="118" x2="270" y2="118" stroke="#aab4bd"/>
    <rect x="40" y="28" width="18" height="90" fill="#3aa53a"/><rect x="100" y="66" width="18" height="52" fill="#1c6cc0"/><rect x="160" y="48" width="18" height="70" fill="#f0a020"/><rect x="220" y="104" width="18" height="14" fill="#d8322f"/>
    <g fill="#fff" stroke="#aab4bd" stroke-width=".6"><rect x="38" y="14" width="22" height="10"/><rect x="98" y="52" width="22" height="10"/><rect x="158" y="34" width="22" height="10"/><rect x="218" y="90" width="22" height="10"/></g>
    <g font-size="5.5" fill="#222a30" text-anchor="middle" font-family="Open Sans, sans-serif"><text x="49" y="21">80</text><text x="109" y="59">35</text><text x="169" y="41">50</text><text x="229" y="97">8</text>
    <g fill="#5b6168" font-size="4.5"><text x="49" y="126">Category 1</text><text x="109" y="126">Category 2</text><text x="169" y="126">Category 3</text><text x="229" y="126">Category 4</text></g></g>
  </svg>
  <div class="abs" style="left:236px;top:212px;width:296px;height:46px;background:#eceef0"></div>
  <svg class="abs" style="left:248px;top:224px" width="200" height="22" viewBox="0 0 200 22"><circle cx="11" cy="11" r="10" fill="#1c6cc0"/><circle cx="131" cy="11" r="10" fill="#1c6cc0"/><path d="M6 14l4-4 3 3 4-5" stroke="#fff" fill="none" stroke-width="1.4"/><path d="M127 7h8v8h-8z" stroke="#fff" fill="none" stroke-width="1.4"/></svg>
  <div class="abs body" style="left:276px;top:220px;width:90px"><b style="color:var(--blue)">Lorem ipsum dolor</b>Steady gains over three years.</div>
  <div class="abs body" style="left:396px;top:220px;width:90px"><b style="color:var(--blue)">Lorem ipsum dolor</b>Low debt across the portfolio.</div>
  <div class="brand-mark" style="font-size:6px">TARN RIDGE</div>
</section>

<section class="slide" style="left:626px;top:2915px">
  <div class="photo" role="img" aria-label="Country road lined with autumn trees" style="inset:0;background:linear-gradient(180deg,#6d8396 0%,#b98a43 45%,#8a5a26 75%,#4a3a2a 100%)"></div>
  <div class="abs" style="left:0;top:130px;width:552px;height:96px;background:rgba(255,255,255,.45)"></div>
  <div class="abs" style="left:0;right:0;top:138px;text-align:center;font-size:34px;font-weight:600;color:#4d545b">Thank You!</div>
  <div class="abs" style="left:0;right:0;top:190px;text-align:center;font-size:9px;font-weight:700;color:var(--blue)">TARN RIDGE PARTNERS</div>
  <div class="abs" style="left:0;top:284px;width:552px;height:27px;background:#3a3f46"></div>
  <div class="contact" style="left:30px;top:292px"><i></i>hello@tarnridge.com</div>
  <div class="contact" style="left:200px;top:292px"><i></i>https://tarnridge.com</div>
  <div class="contact" style="left:420px;top:292px"><i></i>(312) 555-0148</div>
</section>

</body>
</html>
```